Brochure to Describe Meridian 300 Executive Program

I would like a 4 page design.

PAGE 1 = cover
PAGES 2 - 3 = content
PAGE 4 = back

The content for the brochure is attached as PDF and Microsoft Publisher named "Executive Council.VRAL.onepage".

I've also attached past brochures that we've used.

I've also attached some art that we've used. The idea of "Steering Steadfast Outcomes" and a race car is used extensively in our messaging.
Updates

We want very clean, modern 4 page brochures for corporate audience. We want very "flat" clean design. For example, we like the following:
- http://www.clipwall.example/pin/902114573300218467/
- http://www.clipwall.example/pin/720461193388502614/
- http://www.clipwall.example/pin/61827430099145362/
- http://www.clipwall.example/pin/47720318865092146/
- http://www.clipwall.example/pin/274408119653027791/

Final deliverable must be in source .ai or .indd files. so that we can tweak and modify after the project.

Target Market(s)

Meridian 300 executives who operate the more "conservative" functions in the organization such as:
- Chief Audit Executive
- Chief Compliance Officer
- Chief Risk Officer

Industry/Entity Type

Council

Requirements
Must have
• 48 hour turnaround.

Consistent with the design of http://www.vral-example.org. Please use colors from website. May also use the "rainbow" bar colors at the top. Just use a color picker to get the right hex and translate into RGB.

Must provide final in Adobe Illustrator, Adobe InDesign or Microsoft Publisher format.
Nice to have
• Here is a video about a metaphor that we've considered (weaving together Meridian 300 executive jobs/roles into a strong rope) that would be cool to incorporate.

http://presentations.vral-example.org/rope-metaphor

```html
<!DOCTYPE html>
<html lang="en">
<head>
<meta charset="utf-8">
<title>Executive Council – Back Page</title>
<link rel="stylesheet" href="https://fonts.googleapis.com/css2?family=Arimo:wght@400;700&display=swap">
<style>
  :root {
    --brand-red: #cc2229;
    --brand-red-dark: #a81a22;
    --photo-deep: #7a1c22;
    --photo-mid: #b8323a;
    --photo-light: #d9d4d2;
    --ink: #3f3f3f;
    --ink-strong: #333333;
    --white: #ffffff;
    --rule: rgba(255,255,255,0.45);
  }
  * { margin: 0; padding: 0; box-sizing: border-box; }
  html, body { width: 849px; height: 1200px; overflow: hidden; background: var(--white); }
  body { font-family: "Arimo", Arial, sans-serif; position: relative; color: var(--ink); }

  .hero { position: absolute; left: 0; top: 58px; width: 849px; height: 562px; }
  .hero-panel {
    position: absolute; left: 0; top: 0; width: 403px; height: 562px;
    background: var(--brand-red); color: var(--white); padding: 40px 32px 0 80px;
  }
  .hero-photo {
    position: absolute; left: 403px; top: 0; width: 446px; height: 562px;
    background: linear-gradient(160deg, var(--photo-deep) 0%, var(--photo-mid) 45%, #c9454c 65%, var(--photo-light) 100%);
  }
  .panel-heading { font-size: 12px; font-weight: 700; letter-spacing: 0.2px; line-height: 16px; margin-bottom: 8px; }
  .panel-list { list-style: none; font-size: 11px; line-height: 21.5px; opacity: 0.92; }
  .panel-list li::before { content: "• "; }
  .panel-list em { font-style: italic; }
  .panel-rule { border: 0; border-top: 1px dotted var(--rule); width: 290px; margin: 12px 0 16px; }

  .hero-shadow {
    position: absolute; left: 80px; top: 620px; width: 690px; height: 16px;
    background: radial-gradient(ellipse at top, rgba(0,0,0,0.14) 0%, rgba(0,0,0,0) 70%);
  }

  .join { position: absolute; top: 672px; }
  .join-who { left: 80px; width: 300px; }
  .join-how { left: 403px; width: 360px; }
  .join-title { color: var(--brand-red); font-size: 20px; font-weight: 700; margin-bottom: 12px; }
  .join-list { list-style: none; font-size: 14.5px; line-height: 21.5px; color: var(--ink); }
  .join-who .join-list li { margin-bottom: 7px; }
  .join-how .join-list li { margin-bottom: 6px; padding-left: 11px; text-indent: -11px; }
  .join-list li::before { content: "• "; }

  .contact { display: flex; margin-top: 30px; font-size: 14.5px; line-height: 21.5px; }
  .contact-label { color: var(--brand-red); font-weight: 700; width: 84px; flex: none; }
  .contact-name { font-weight: 700; color: var(--ink-strong); }
</style>
</head>
<body>
  <section class="hero">
    <div class="hero-panel">
      <h3 class="panel-heading">2014 SUGGESTED CYCLES</h3>
      <ul class="panel-list">
        <li>Setting Objectives and Assessing Performance</li>
        <li>Addressing Internal and External Uncertainty</li>
        <li>Improving Culture and Engagement</li>
        <li>Ensuring Effective Reports and Communication</li>
        <li>Selecting and Using the Right Analytics</li>
        <li>Leaning the GRC</li>
        <li>Capability</li>
      </ul>
      <hr class="panel-rule">
      <h3 class="panel-heading">2014 IN PERSON EVENTS</h3>
      <ul class="panel-list">
        <li>Kick off session in January Location and date tbd</li>
        <li>Washington D.C. - <em>May 21-22</em></li>
        <li>Scottsdale, Arizona, - <em>November 6-7</em></li>
      </ul>
      <hr class="panel-rule">
      <h3 class="panel-heading">HOW THE EXECUTIVE COUNCIL<br>IS DIFFERENT</h3>
      <ul class="panel-list">
        <li>Executives across all GRC roles participate</li>
        <li>Small group supports deeper interaction</li>
        <li>Surveys, tools and resources are based on Council member needs</li>
        <li>Resources are deliv-ered that can be used in-house as is or with customization support</li>
      </ul>
    </div>
    <div class="hero-photo" role="img" aria-label="Photograph of a pit crew changing a tyre on a red race car with the driver in the cockpit"></div>
  </section>
  <div class="hero-shadow"></div>

  <section class="join join-who">
    <h2 class="join-title">Who Should Join?</h2>
    <ul class="join-list">
      <li>Strategic Leaders</li>
      <li>Management Committee Members</li>
      <li>Chief Risk Officers</li>
      <li>Chief Ethics &amp; Compliance Officers</li>
      <li>Chief Audit Executives</li>
      <li>General Counsels</li>
      <li>Chief Information Officers</li>
    </ul>
  </section>

  <section class="join join-how">
    <h2 class="join-title">How to Join?</h2>
    <ul class="join-list">
      <li>Membership is restricted to invited senior executives</li>
      <li>Individuals may submit their own names for consideration, or may be nominated by their immediate superior or by other Council members</li>
      <li>Seats are limited</li>
    </ul>
    <div class="contact">
      <div class="contact-label">Contact:</div>
      <div class="contact-details">
        <div class="contact-name">VRAL Chair, Daniel Marlow:</div>
        <div>dmarlow@vral.org</div>
        <div class="contact-name">or VRAL President, Helen Brandt:</div>
        <div>hbrandt@vral.org</div>
      </div>
    </div>
  </section>
</body>
</html>
```